IT Professional business card with a hometown feel and a little edgy.

My business name is Tamble Website Solutions. But I have ended up doing much more. I live in a very small remote community, where everyone knows everyone. We like the one-on-one customer service in this community. I do computer tutoring, virus removal, networking, and software training. My clients are businesses and private individuals.

My website is tamblewebsitesolutions.example, when I first designed it I was going for a fresh, clean look, which I still like. But I am thinking about making the website a bit more edgy to match my new logo from ArtHively (logo attached). At this time my website does not display the new logo, but I plan on redesigning the website in the future to match the logo and business card.

My tag line is "let the internet work for you"

I'm thinking I would like to have the business card printed with a metallic finish.
Updates

Please do not use black backgrounds, or any solid dark colors. Prefer light or white backgrounds.

Target Market(s)

Small businesses. Individuals that need computer help at home.

Industry/Entity Type

It Company

Contact Information for Business Card

Nora Prandell
Tamble Website Solutions
PO Box 7153
Cedar Hollow, WA 98765
Cell: 555-271-3096
nora@tamblewebsitesolutions.example
tamblewebsitesolutions.example

Font styles to use
Serif

Requirements
Must have
• Must have all the information listed in "Business Card Details"
• Must use the logo provided.
• Use the colors from the provided logo
Nice to have
• Would like to use my tagline "let the internet work for you" all lowercase

```html
<!DOCTYPE html>
<html lang="en">
<head>
<meta charset="utf-8">
<title>Tamble Website Solutions – Business Card</title>
<link rel="stylesheet" href="https://fonts.googleapis.com/css2?family=Source+Sans+3:wght@400;600&display=swap">
<style>
  :root {
    --backdrop-top: #2a2a2a;
    --backdrop-bottom: #070707;
    --card-light: #f3f3f3;
    --brand-green: #2f6b2f;
    --ink: #1b1b1b;
    --face-top: #7aae68;
    --face-bottom: #245a2c;
    --white: #ffffff;
  }
  * { margin: 0; padding: 0; box-sizing: border-box; }
  html, body { width: 1200px; height: 900px; overflow: hidden; }
  body {
    position: relative;
    background: linear-gradient(180deg, var(--backdrop-top) 0%, var(--backdrop-bottom) 100%);
    font-family: "Source Sans 3", "Myriad Pro", Arial, sans-serif;
  }
  .card {
    position: absolute;
    top: 184px;
    height: 490px;
    border-radius: 12px;
    box-shadow: 0 2px 10px rgba(0,0,0,0.5);
  }
  .card-back {
    left: 299px;
    width: 301px;
    background: var(--card-light);
    color: var(--ink);
    text-align: center;
  }
  .card-front {
    left: 645px;
    width: 304px;
    background: linear-gradient(180deg, var(--face-top) 0%, var(--face-bottom) 100%);
  }
  .brand-mark { position: absolute; }
  .brand-name {
    position: absolute;
    text-align: left;
    font-weight: 400;
    white-space: nowrap;
  }
  .card-back .brand-mark { left: 62px; top: 262px; top: 64px; width: 56px; height: 56px; background: var(--brand-green); }
  .card-back .brand-name { left: 193px; top: 79px; font-size: 16px; line-height: 17px; color: var(--brand-green); }
  .card-front .brand-mark { left: 62px; top: 200px; width: 66px; height: 66px; background: var(--white); }
  .card-front .brand-name { left: 200px; top: 216px; font-size: 18px; line-height: 19px; color: var(--white); }

  .person-name {
    position: absolute; left: 0; right: 0; top: 226px;
    font-size: 20px; font-weight: 600; color: var(--brand-green);
  }
  .contact-list {
    position: absolute; left: 0; right: 0; top: 288px;
    list-style: none; font-size: 14px; line-height: 20px;
  }
  .contact-list li { display: flex; justify-content: center; align-items: center; gap: 5px; }
  .contact-icon { width: 10px; height: 10px; fill: var(--ink); }
  .company-name {
    position: absolute; left: 0; right: 0; top: 388px;
    font-size: 17px; font-weight: 600; color: var(--brand-green);
  }
  .postal-address {
    position: absolute; left: 0; right: 0; top: 425px;
    font-style: normal; font-size: 14px; line-height: 20px;
  }
</style>
</head>
<body>
  <section class="card card-back">
    <span class="brand-mark"></span>
    <span class="brand-name">Tamble<br>Website<br>Solutions</span>

    <h1 class="person-name">Nora Prandell</h1>

    <ul class="contact-list">
      <li>
        <svg class="contact-icon" viewBox="0 0 10 10" aria-hidden="true"><path d="M1 3 Q5 0 9 3 L8 4.5 L6.5 3.8 L6.5 3 Q5 2.5 3.5 3 L3.5 3.8 L2 4.5 Z M2.5 5 L7.5 5 L8.5 9 L1.5 9 Z"/></svg>
        555-271-3096
      </li>
      <li>
        <svg class="contact-icon" viewBox="0 0 10 10" aria-hidden="true"><path d="M0.5 2 H9.5 V8 H0.5 Z M1 2.5 L5 5.5 L9 2.5" stroke="#f3f3f3" stroke-width="0.7"/></svg>
        nora@tamblewebsitesolutions.example
      </li>
      <li>
        <svg class="contact-icon" viewBox="0 0 10 10" aria-hidden="true"><path d="M4 6 L6 4 M3.5 4.5 L1.8 6.2 A1.4 1.4 0 0 0 3.8 8.2 L5.5 6.5 M6.5 5.5 L8.2 3.8 A1.4 1.4 0 0 0 6.2 1.8 L4.5 3.5" fill="none" stroke="#1b1b1b" stroke-width="1.1"/></svg>
        www.tamblewebsitesolutions.example
      </li>
    </ul>

    <h2 class="company-name">Tamble Website Solutions</h2>

    <address class="postal-address">PO Box 7153<br>Cedar Hollow, WA 98765</address>
  </section>

  <section class="card card-front">
    <span class="brand-mark"></span>
    <span class="brand-name">Tamble<br>Website<br>Solutions</span>
  </section>
</body>
</html>
```